Etiketten für Ätherische Öle, Extrakte und Speiseöle gesucht
Zielgruppe
Wir verkaufen natürlich Produkte. Ätherische öle, Extrakte, Speise öle.
Wir verkaufen im Webshop, Kaufwelt und auch im Betrieb.
https://www.natur-sefo.com
Wir verkaufen hauptsächlich innerhalb Italiens und Deutschland daher doppel sprachig.
Aufgabenstellung
Guten Tag
Bitte verwenden Sie! : * beispiel_10_ml_etikett_nachbau.jpg *
Da mir die kleinste Größe die wichtigste ist habe ich ein beispiel Hochgeladen. Das kleinste Etikett lässt sich öffnen und daher sind nur 7 cm ersichtlich und man muss das Etikett aufmachen.
Habe ein Beispiel Hochgeladen. Aber bitte einfach kreativ sein. *Anhang: beispiel Etikett*
Sobald ich eine Art vom kelinsten habe würde ich dies für die 2 anderen Größen übernehmen aber das man Sie irgendwie gut unterscheiden kann da dies dann komplett andere Produkte (Extrakte/Speise öl) sein werden.
Erstellung von drei unterschiedlichen Größen von Etiketten mit folgenden Eigenschaften:
Am wichtigsten ist mir das kleinste Etikett da dies auch am schwersten ist daher habe ich die anderen Größen nun gelöscht!
• 10 ml Länge: 155 mm Breite: 32 mm.
Brauche 3 unterschiedliche Grund Farben: z. B. Ätherische Öle (Grün) Extrakte (Rot) Speiseöle (gelb). Die Farben lasse ich sie entscheiden.
Die Etiketten müssen 2 Sprachen (Deutsch / Italienisch) sein deshalb muss dieses berücksichtigt werden.
Anbei finden Sie:
• Logo (Bild Logo)
• Beispiel Text ätherische Öle
• Bilder der aktuellen Flaschen
Unter https://www.natur-sefo.com/de finden Sie meine Seite
Anmerkung: Im Anhang: *Back*
Habe ich mein Logo mit Firmennamen ; Bio des Hollmer Tobias
Da ich jedoch nicht alle Produkte im biologischen Anbau habe und mein Logo zu miss Verständnis führen könnte habe ich ein Bildliches Logo gemacht das ich fortan auf meinen Produkten haben möchte. Im besonderes dieses Grün das in beiden vorhanden ist versuche ich zu integrieren.
Habe selbst ein Etikett designet das aber sehr unprofessionell wirkt aber dieses Grüne das ich gerne als merkmal unterbringen würde.
Siehe Anhang: neemöl

```html
<!DOCTYPE html>
<html lang="de">
<head>
<meta charset="utf-8">
<title>Lavandula Angustifolia – Etikett 10 ml (155 × 32 mm)</title>
<link href="https://fonts.googleapis.com/css2?family=Poppins:wght@300;400;500;600&display=swap" rel="stylesheet">
<style>
  :root {
    --ink: #2e3a8c;
    --ink-body: #2c3592;
    --frame: #e5197a;
    --label-yellow: #f4ee00;
    --label-white: #ffffff;
    --date-field: #fbf9b2;
    --logo-line: #b9cf94;
    --logo-ink: #6e6e6e;
    --divider: #b8b36a;
    --page: #f2f2f2;
  }
  * { box-sizing: border-box; margin: 0; padding: 0; }
  html, body {
    width: 1200px; height: 494px; overflow: hidden;
    background: var(--page);
    font-family: "Poppins", sans-serif;
    color: var(--ink-body);
  }

  /* 155 × 32 mm label, scaled to 1170 × 242 px */
  .label {
    position: absolute; left: 15px; top: 126px; width: 1170px; height: 242px;
    background: linear-gradient(to bottom,
      var(--label-white) 0px, var(--label-white) 70px,
      #fbf7a0 100px, var(--label-yellow) 140px, var(--label-yellow) 242px);
  }
  .label__frame {
    position: absolute; left: 6px; top: 6px; right: 6px; bottom: 6px;
    border: 2px solid var(--frame);
  }

  /* left: brand + company */
  .brand-mark {
    position: absolute; left: 20px; top: 16px; width: 72px; height: 64px;
    border: 1px solid var(--logo-line); background: var(--label-white);
    display: flex; align-items: center; justify-content: center; text-align: center;
    font-size: 9.5px; line-height: 1.3; color: var(--logo-ink); padding: 4px;
  }
  .company {
    position: absolute; left: 20px; top: 90px; width: 240px;
    font-style: normal; font-size: 9.2px; line-height: 11.8px;
  }
  .company__title { font-weight: 600; }

  /* centre: product */
  .product-name {
    position: absolute; left: 270px; top: 16px; width: 350px; text-align: center;
    font-weight: 300; font-size: 46px; line-height: 1; color: var(--ink);
  }
  .product-species {
    position: absolute; left: 270px; top: 70px; width: 350px; text-align: center;
    font-size: 15px; letter-spacing: 8px; color: var(--ink);
  }
  .product-visual {
    position: absolute; left: 415px; top: 118px; width: 60px; height: 60px;
    background: var(--label-white); padding: 3px;
  }
  .product-visual__fill {
    width: 100%; height: 100%;
    background: radial-gradient(circle at 50% 40%, #c56fd8 0%, #7c67c9 35%, #d9e8c7 62%, #9dc25a 100%);
  }
  .volume {
    position: absolute; left: 395px; top: 186px; width: 100px; text-align: center;
    font-size: 17px; font-weight: 300;
  }

  /* right: bilingual text */
  .lang {
    position: absolute; top: 16px; width: 250px;
    font-size: 8.6px; line-height: 10.8px;
  }
  .lang--de { left: 636px; }
  .lang--it { left: 904px; }
  .lang__code {
    display: inline-block; font-weight: 600; font-size: 8px;
    border: 1px solid var(--ink-body); padding: 0 3px; margin-bottom: 3px; line-height: 10px;
  }
  .lang strong { font-weight: 600; }
  .lang__warning { margin-top: 5px; font-weight: 500; }
  .lang-divider {
    position: absolute; left: 893px; top: 18px; width: 1px; height: 140px;
    background: var(--divider);
  }

  .origin {
    position: absolute; left: 636px; top: 168px; font-size: 10.5px;
  }
  .best-before {
    position: absolute; left: 636px; top: 188px; width: 250px;
    font-size: 8.6px; line-height: 10.8px; font-weight: 500;
  }
  .best-before__field {
    position: absolute; left: 904px; top: 184px; width: 240px; height: 40px;
    background: var(--date-field);
  }
</style>
</head>
<body>
<main class="label">
  <div class="label__frame"></div>

  <div class="brand-mark">Bio d. Hollmer Tobias</div>

  <address class="company">
    <span class="company__title">Firmenname / Ragione sociale:</span><br>
    Bio des Hollmer Tobias<br>
    Talweg 14, I-39088 Feldau<br>
    IVA: IT04518230965<br>
    CF.: HLLTBS90M12F132K<br>
    Tel; +39 0473/512870<br>
    Handy / Cell.; 3408127365<br>
    https://www.natur-sefo.com/<br>
    info.natursefo@postfeld.it
  </address>

  <h1 class="product-name">Lavandula</h1>
  <p class="product-species">Angustifolia</p>
  <div class="product-visual">
    <div class="product-visual__fill" role="img" aria-label="Illustration einer violetten Blüte auf grünem Hügel"></div>
  </div>
  <p class="volume">10 ml</p>

  <section class="lang lang--de" lang="de">
    <span class="lang__code">DE</span>
    <p>100% natürliches etherisches Öl. Aroma-Kosmetikum zur Körperpflege.
    <strong>Anwendung:</strong> Als Haut- u. Massageöl max 15 Tr. mit 50 ml z.B. Mandelöl mischen.
    Als Badezusatz 8-15 Tr. auf 4 Eßl. Sahne oder Milch ins Badewasser geben.</p>
    <p class="lang__warning">Nur in der angegebenen Verdünnung anwenden! Nicht in die Augen oder auf die Schleimhäute bringen! Außer Reichweite von Kindern lagern.</p>
  </section>

  <div class="lang-divider"></div>

  <section class="lang lang--it" lang="it">
    <span class="lang__code">IT</span>
    <p>Olio essenziale 100% naturale. Cosmetico aromatico per la cura del corpo.
    <strong>Uso:</strong> come olio per pelle e massaggi max 15 gocce in 50 ml p.es. di olio di mandorla.
    Nel bagno 8-15 gocce in 4 cucchiai di panna o latte nell'acqua.</p>
    <p class="lang__warning">Usare solo nella diluizione indicata! Evitare il contatto con occhi e mucose! Tenere fuori dalla portata dei bambini.</p>
  </section>

  <p class="origin">Abgefüllt in Italien · Imbottigliato in Italia</p>
  <p class="best-before">Mindestens haltbar bis:<br>Da consumarsi preferibilmente entro:</p>
  <div class="best-before__field"></div>
</main>
</body>
</html>
```